Förderverein einer Kirchengemeinde sucht Flyer-Design
Zielgruppe
Wir sind ein Förderverein einer Kirchengemeinde, der sich für die kirchenmusikalische Arbeit einsetzt.
Wir wünschen uns ein niveauvolles und zeitgemäßes/modernes Flyerdesign, das die etablierten Konzertbesucher anspricht, aber vor allem auch Menschen erreicht und überzeugt, die (noch) nichts mit Kirche zu tun haben.
Das Alter der (Haupt-) Zielgruppe (Männer und Frauen) erstreckt sich von 45 bis 70 Jahren.
Aufgabenstellung
Bei der Wahl des Formates würden wir (aus der Sicht von Laien) ein zweimal gefaltetes DIN A4 quer Format nehmen. Aber wir lassen uns gerne überraschen und sind grundsätzlich für andere Lösungen offen.
Bitte den Abschnitt für Adress- und sonstige Dateneintragungen samt Kontodaten so gestalten und platzieren, dass man ihn leicht abtrennen und verschicken kann.
Der Flyer soll Kirchenmusik als lebendig und attraktiv darstellen und neue (jüngere) Mitglieder für den Freundeskreis werben.
Lassen Sie die Bilder sprechen!!

```html
<!DOCTYPE html>
<html lang="de">
<head>
<meta charset="utf-8">
<title>Musikkreis Lumevano – Flyer</title>
<link href="https://fonts.googleapis.com/css2?family=Nunito+Sans:ital,wght@0,400;0,600;1,400&family=Herr+Von+Muellerhoff&display=swap" rel="stylesheet">
<style>
:root{
  --olive-dark:#47462f;
  --olive-light:#6d6b49;
  --field:#e6e4de;
  --text:#f3f1ea;
  --text-soft:#dcdad0;
  --photo-console:#6e5a2e;
  --photo-group:#6c7a4e;
  --photo-choir:#4b4238;
  --photo-kids:#8a8f47;
  --page:#ffffff;
}
*{margin:0;padding:0;box-sizing:border-box}
html,body{width:1200px;height:819px;overflow:hidden;background:var(--page)}
body{position:relative;font-family:"Nunito Sans",Arial,sans-serif;color:var(--text)}
.spread{position:absolute;left:18px;width:1131px;height:377px;background:var(--olive-dark);overflow:hidden}
.spread--outside{top:8px}
.spread--inside{top:427px}
.facets{position:absolute;inset:0;width:100%;height:100%}
.abs{position:absolute}
.fold{position:absolute;top:0;bottom:0;border-left:1px dashed rgba(255,255,255,.55)}
.form-title{font-style:italic;font-size:8px;letter-spacing:.2px}
.field{position:absolute;height:19px;background:var(--field)}
.field-label{position:absolute;font-size:4.5px;color:var(--text-soft)}
.small{font-size:5.6px;line-height:7.5px;color:var(--text-soft)}
.body-text{font-size:7.3px;line-height:9.6px;color:var(--text)}
.body-text p{margin-bottom:9.5px}
.script{font-family:"Herr Von Muellerhoff",cursive;color:var(--text);white-space:nowrap;line-height:1}
.brand{font-family:"Nunito Sans",Arial,sans-serif;font-weight:400;font-size:22px;line-height:25px;color:#fff}
.list p{margin-bottom:10.5px}
.radio{position:absolute;display:flex;align-items:center;gap:6px;font-size:6.4px;color:var(--text-soft)}
.radio::before{content:"";width:8px;height:8px;border-radius:50%;background:var(--field)}
.section-title{font-style:italic;font-size:9px}
a{color:inherit}
</style>
</head>
<body>

<section class="spread spread--outside">
  <svg class="facets" viewBox="0 0 1131 377" preserveAspectRatio="none" aria-hidden="true">
    <polygon points="0,0 200,0 90,377 0,377" fill="rgba(255,255,255,.03)"/>
    <polygon points="120,377 376,80 376,377" fill="rgba(0,0,0,.12)"/>
    <polygon points="376,377 560,120 754,377" fill="rgba(255,255,255,.04)"/>
    <polygon points="600,0 754,0 754,260" fill="rgba(0,0,0,.1)"/>
    <polygon points="754,349 1131,204 1131,377 754,377" fill="var(--olive-light)"/>
    <polygon points="900,377 1131,250 1131,377" fill="rgba(255,255,255,.06)"/>
  </svg>

  <div class="abs form-title" style="left:60px;top:75px">SEPA-Lastschriftmandat</div>
  <div class="field" style="left:60px;top:88px;width:252px"></div>
  <div class="field-label" style="left:60px;top:109px">IBAN</div>
  <div class="field" style="left:60px;top:118px;width:252px"></div>
  <div class="field-label" style="left:60px;top:139px">BIC</div>
  <div class="field" style="left:60px;top:149px;width:252px"></div>
  <div class="field-label" style="left:60px;top:170px">Kreditinstitut</div>
  <div class="field" style="left:60px;top:180px;width:252px"></div>
  <div class="field-label" style="left:60px;top:201px">Kontoinhaber</div>
  <p class="abs small" style="left:60px;top:222px;width:260px">Hiermit ermächtige ich den Musikkreis Lumevano den von mir zu entrichtenden Mitgliedsbeitrag von meinem Konto einzuziehen.</p>
  <div class="field" style="left:60px;top:253px;width:102px"></div>
  <div class="field-label" style="left:60px;top:274px">Ort, Datum</div>
  <div class="field" style="left:167px;top:253px;width:145px"></div>
  <div class="field-label" style="left:167px;top:274px">Unterschrift</div>
  <p class="abs small" style="left:60px;top:294px">Der Einzug der Mitgliedsbeiträge erfolgt zu Beginn eines Kalenderjahres.</p>

  <div class="fold" style="left:376px"></div>

  <svg class="abs" style="left:376px;top:0" width="220" height="172" viewBox="0 0 220 172" role="img" aria-label="Foto: Spieltisch der Orgel mit Registerzügen">
    <defs><linearGradient id="consoleTone" x1="0" y1="0" x2="1" y2="1"><stop offset="0" stop-color="#b59a3e"/><stop offset="1" stop-color="var(--photo-console)"/></linearGradient></defs>
    <polygon points="0,0 220,0 220,62 0,170" fill="url(#consoleTone)"/>
  </svg>
  <div class="abs script" style="left:588px;top:106px;font-size:26px">Spendenkonto</div>
  <div class="abs body-text" style="left:590px;top:136px">
    Heidebank Nord<br>IBAN: DE00123456780012345678<br>BIC: HEIDDE21XXX<br><br>Verwendungszweck bei Einzelspenden<br>unter Angabe der Kostenstelle.
  </div>
  <div class="abs body-text" style="left:427px;top:241px;width:310px">
    <p>Wenn Sie die Kirchenmusik an St. Marien als Mitglied im Musikkreis Lumevano fördern möchten, senden Sie das ausgefüllte Formular auf der Rückseite an den</p>
    <p>Musikkreis Lumevano<br>Kirchengemeinde St. Marien<br>Lindenweg 7, 12345 Musterstadt</p>
    <p>Tel.: 01234-56 78 90, info@musikkreis-lumevano.de</p>
    <p>Nähere Informationen zur Kirchenmusik an St. Marien und<br>zum Musikkreis finden Sie unter <a href="#">www.kirchenmusik-musterstadt.de</a></p>
  </div>

  <svg class="abs" style="left:754px;top:0" width="377" height="350" viewBox="0 0 377 350" role="img" aria-label="Foto: historische Barockorgel mit goldenen Verzierungen">
    <defs><linearGradient id="organTone" x1="0" y1="0" x2="0" y2="1"><stop offset="0" stop-color="#a38f5c"/><stop offset=".5" stop-color="#9a7a68"/><stop offset="1" stop-color="#8f9085"/></linearGradient></defs>
    <polygon points="0,0 377,0 377,204 0,349" fill="url(#organTone)"/>
  </svg>
  <div class="abs brand" style="left:866px;top:170px">Musikkreis<br>Lumevano</div>
  <div class="abs script" style="left:905px;top:285px;font-size:40px;line-height:30px;transform:rotate(-16deg);transform-origin:left top">Kirchenmusik<br>&nbsp;braucht Freunde!</div>
</section>

<section class="spread spread--inside">
  <svg class="facets" viewBox="0 0 1131 377" preserveAspectRatio="none" aria-hidden="true">
    <polygon points="0,0 260,0 120,377 0,377" fill="rgba(255,255,255,.03)"/>
    <polygon points="180,377 560,40 610,377" fill="rgba(0,0,0,.1)"/>
    <polygon points="560,0 754,0 754,377 700,377" fill="rgba(255,255,255,.03)"/>
    <polygon points="754,0 1131,0 1131,377 950,377" fill="rgba(255,255,255,.04)"/>
    <polygon points="1000,377 1131,180 1131,377" fill="var(--olive-light)"/>
  </svg>

  <div class="abs script" style="left:22px;top:44px;font-size:32px;line-height:26px;transform:rotate(-16deg);transform-origin:left top">Mitglieder haben<br>&nbsp;gute Gründe</div>
  <div class="abs body-text" style="left:45px;top:96px;font-weight:600;font-style:italic">Sie…</div>
  <div class="abs body-text list" style="left:45px;top:120px;width:160px">
    <p>… erhalten ermäßigte Eintrittspreise von<br>&nbsp;&nbsp;&nbsp;gemeindeeigenen Konzerten</p>
    <p>… können Konzertkarten vor dem<br>&nbsp;&nbsp;&nbsp;öffentlichen Verkauf erwerben</p>
    <p>… gestalten die Arbeit des Musik-<br>&nbsp;&nbsp;&nbsp;kreises in den jährlichen Mitglieder-<br>&nbsp;&nbsp;&nbsp;versammlungen aktiv mit</p>
    <p>… erhalten aktuelle Informationen<br>&nbsp;&nbsp;&nbsp;über Veranstaltungen der Gemeinde<br>&nbsp;&nbsp;&nbsp;bequem per Email und profitieren<br>&nbsp;&nbsp;&nbsp;so zu allererst</p>
    <p>… können den Mitgliedsbeitrag<br>&nbsp;&nbsp;&nbsp;steuerlich absetzen und erhalten<br>&nbsp;&nbsp;&nbsp;eine Spendenbescheinigung</p>
    <p>… können an Ausflügen des<br>&nbsp;&nbsp;&nbsp;Musikkreises teilnehmen</p>
  </div>

  <svg class="abs" style="left:222px;top:0" width="360" height="365" viewBox="0 0 360 365" aria-hidden="true">
    <polygon role="img" aria-label="Foto: Flötenensemble im Garten" points="1,14 171,3 175,125 1,137" fill="var(--photo-group)"/>
    <polygon role="img" aria-label="Foto: Posaunenchor mit Blechblasinstrumenten" points="128,108 228,88 336,104 336,235 140,240" fill="#7f7f6d"/>
    <polygon role="img" aria-label="Foto: Kantorei im Kirchenraum" points="10,190 174,197 172,296 8,296" fill="var(--photo-choir)"/>
    <polygon role="img" aria-label="Foto: Kinderchor in gelben T-Shirts" points="150,262 224,255 303,268 300,360 150,355" fill="var(--photo-kids)"/>
  </svg>

  <div class="abs script" style="left:446px;top:46px;font-size:28px;line-height:22px;transform:rotate(-14deg);transform-origin:left top">Kirchenmusik<br>&nbsp;braucht Freunde</div>
  <div class="abs body-text list" style="left:590px;top:51px;width:150px">
    <p>Im Jahr 1999 gegründet, unterstützt der Musikkreis Lumevano die vielfältigen musikalischen Aktivitäten an der St. Marien-Kirche.</p>
    <p>Wir laden Sie ein, Mitglied zu werden!</p>
    <p>Mit Ihrem Beitrag …</p>
    <p>… bereichern Sie Musterstadts kulturelle<br>&nbsp;&nbsp;&nbsp;Landschaft durch den Erhalt und<br>&nbsp;&nbsp;&nbsp;Ausbau unseres hohen<br>&nbsp;&nbsp;&nbsp;kirchenmusikalischen Niveaus</p>
    <p>… stärken Sie das Ehrenamt</p>
    <p>… ermöglichen Sie der Kantorei, dem<br>&nbsp;&nbsp;&nbsp;Posaunenchor, dem Kinderchor und<br>&nbsp;&nbsp;&nbsp;dem Flötenensemble regelmäßige<br>&nbsp;&nbsp;&nbsp;Probenarbeit, Probenwochenenden<br>&nbsp;&nbsp;&nbsp;und die Anschaffung von Notenmaterial</p>
    <p>… erhalten Sie die historische Johann<br>&nbsp;&nbsp;&nbsp;Lindner Orgel von 1748</p>
    <p>… fördern Sie die Ausbildung<br>&nbsp;&nbsp;&nbsp;kirchenmusikalischen Nachwuchses</p>
  </div>

  <div class="fold" style="left:754px"></div>

  <div class="abs section-title" style="left:804px;top:20px">Beitrittserklärung</div>
  <div class="field" style="left:804px;top:36px;width:283px"></div><div class="field-label" style="left:804px;top:56px">Name, Vorname</div>
  <div class="field" style="left:804px;top:63px;width:283px"></div><div class="field-label" style="left:804px;top:83px">für die Institution/Firma + persönlich</div>
  <div class="field" style="left:804px;top:90px;width:283px"></div><div class="field-label" style="left:804px;top:110px">Straße, Hausnr.</div>
  <div class="field" style="left:804px;top:118px;width:283px"></div><div class="field-label" style="left:804px;top:138px">PLZ, Ort</div>
  <div class="field" style="left:804px;top:145px;width:283px"></div><div class="field-label" style="left:804px;top:165px">Telefon/Handy</div>
  <div class="field" style="left:804px;top:173px;width:283px"></div><div class="field-label" style="left:804px;top:193px">Emailadresse</div>
  <div class="field" style="left:804px;top:200px;width:283px"></div><div class="field-label" style="left:804px;top:220px">Geburtstag</div>
  <div class="field" style="left:804px;top:228px;width:101px"></div><div class="field-label" style="left:804px;top:249px">Datum</div>
  <div class="field" style="left:912px;top:228px;width:175px"></div><div class="field-label" style="left:912px;top:249px">Unterschrift</div>

  <div class="abs section-title" style="left:804px;top:264px">Mitgliedsbeiträge</div>
  <div class="radio" style="left:803px;top:287px">jeweils Mindestbeiträge</div>
  <div class="radio" style="left:803px;top:304px">Ehepaare/Partnerschaften 32€</div>
  <div class="radio" style="left:803px;top:321px"></div>
  <div class="field" style="left:818px;top:316px;width:74px;height:17px"></div>
  <div class="abs small" style="left:895px;top:321px">€</div>
  <div class="field-label" style="left:818px;top:336px">Bitte frei wählbaren Betrag einfügen</div>
  <div class="radio" style="left:803px;top:351px">Einmalige Spende (ohne Mitgliedschaft)</div>
  <div class="radio" style="left:937px;top:287px">Einzelpersonen 20 €</div>
  <div class="radio" style="left:937px;top:304px">Institutionen/Firmen 95 €</div>
  <div class="radio" style="left:937px;top:321px">ich benötige eine Spendenbescheinigung</div>
</section>

</body>
</html>
```